Garden Design Business Card Design

A business card design for garden design company called ;
ROOTS AND RAKE which has a great deal of maintenance but
wishes to promote its expertise for design in planting and garden
design, but in an informal manner.

Would love to see quite a rustic approach,very strong and innovative and taking risks on typography. Am open to ideas with
colours,as memorability is important.

Target Market(s)

General public 40/50 years in a very trendy area

Industry/Entity Type

Business

Contact Information for Business Card

ROOTS AND RAKE. Garden design and maintenance.
Peter Holcombe
Telephone 01632 960417 Mobile 07700 900583

```html
<!DOCTYPE html>
<html lang="en">
<head>
<meta charset="utf-8">
<title>Roots and Rake – Business Card</title>
<link href="https://fonts.googleapis.com/css2?family=Cinzel:wght@400&family=Open+Sans:wght@400&display=swap" rel="stylesheet">
<style>
  :root {
    --backdrop: #3a3a3c;
    --leaf-light: #a3bd3b;
    --leaf-mid: #7fa536;
    --leaf-deep: #5a8832;
    --ink-white: #ffffff;
  }
  html, body {
    margin: 0;
    width: 1200px;
    height: 999px;
    overflow: hidden;
    background: var(--backdrop);
  }
  .business-card {
    position: absolute;
    left: 75px;
    top: 200px;
    width: 1050px;
    height: 600px;
    overflow: hidden;
    color: var(--ink-white);
    background: linear-gradient(to bottom, var(--leaf-light) 0%, var(--leaf-deep) 55%, var(--leaf-deep) 100%);
  }
  .lower-field {
    position: absolute;
    left: 0;
    right: 0;
    top: 270px;
    bottom: 0;
    background: linear-gradient(to bottom, var(--leaf-deep) 0%, var(--leaf-light) 35%, var(--leaf-mid) 100%);
  }
  .brand-name {
    position: absolute;
    left: 0;
    right: 0;
    top: 52px;
    margin: 0;
    text-align: center;
    font-family: "Cinzel", serif;
    font-weight: 400;
    font-size: 92px;
    letter-spacing: 1px;
    line-height: 1;
    white-space: nowrap;
  }
  .tagline {
    position: absolute;
    left: 0;
    right: 0;
    top: 160px;
    margin: 0;
    text-align: center;
    font-family: "Open Sans", sans-serif;
    font-size: 38px;
    line-height: 1;
    white-space: nowrap;
  }
  .contact-block {
    position: absolute;
    right: 55px;
    top: 385px;
    font-family: "Open Sans", sans-serif;
    white-space: nowrap;
  }
  .contact-name {
    margin: 0 0 20px;
    font-size: 40px;
    line-height: 1;
  }
  .contact-line {
    display: flex;
    align-items: center;
    gap: 14px;
    margin: 0 0 8px;
    font-size: 28px;
    line-height: 1.1;
  }
  .contact-icon {
    width: 24px;
    height: 24px;
    flex: none;
  }
</style>
</head>
<body>
  <div class="business-card">
    <div class="lower-field" role="img" aria-label="Decorative sweeping curve over layered green fields"></div>

    <h1 class="brand-name">ROOTS AND RAKE</h1>
    <p class="tagline">Garden design and maintenance</p>

    <div class="contact-block">
      <p class="contact-name">Peter Holcombe</p>
      <p class="contact-line">
        <svg class="contact-icon" viewBox="0 0 24 24" aria-label="Telephone">
          <path d="M6 3 L9 3 L10.5 7.5 L8.5 9 C9.5 11.5 12 14 14.5 15 L16 13 L20.5 14.5 L20.5 18 C20.5 19.5 19 21 17 20.5 C10 19 5 14 3.5 7 C3 5 4.5 3 6 3 Z" fill="none" stroke="#fff" stroke-width="2" stroke-linejoin="round"/>
          <path d="M14 3.5 A7 7 0 0 1 20.5 10 M14 7 A3.5 3.5 0 0 1 17 10" fill="none" stroke="#fff" stroke-width="1.8" stroke-linecap="round"/>
        </svg>
        01632 960417
      </p>
      <p class="contact-line">
        <svg class="contact-icon" viewBox="0 0 24 24" aria-label="Mobile">
          <rect x="4" y="2.5" width="16" height="19" rx="3" fill="none" stroke="#fff" stroke-width="2.2"/>
          <path d="M8 17 L16 7" stroke="#fff" stroke-width="1.6" stroke-linecap="round"/>
        </svg>
        07700 900583
      </p>
    </div>
  </div>
</body>
</html>
```